lantern institute of business and technology web site

I need web site for the institute which focus on business courses and computer course it is also for vocation train for employment It is also carear development and advancement .It should have links to online study resource which free
Industry/Entity Type
Business
Number of Pages Required
1 page
Look and feel

```html
<!DOCTYPE html>
<html lang="en">
<head>
<meta charset="utf-8">
<title>Lantern Institute of Business and Technology</title>
<link href="https://fonts.googleapis.com/css2?family=Open+Sans:wght@400;600;700;800&display=swap" rel="stylesheet">
<style>
:root{
  --blue:#1f6fc5;
  --blue-dark:#0d4f9e;
  --sky:#1a8fe0;
  --navy:#14213a;
  --navy-deep:#0c1628;
  --ink:#333a44;
  --muted:#6b7480;
  --line:#d9dee5;
  --pale:#f3f6fa;
  --white:#ffffff;
}
*{box-sizing:border-box;margin:0;padding:0}
html,body{width:1200px;height:2452px;overflow:hidden}
body{font-family:"Open Sans",Arial,sans-serif;color:var(--ink);background:var(--white);font-size:13px;line-height:1.55}
.wrap{width:1080px;margin:0 auto;position:relative}

/* header */
.site-header{height:88px;background:var(--white);position:relative;border-bottom:3px solid var(--blue)}
.topline{height:32px;display:flex;align-items:center;justify-content:space-between;font-size:12px;color:var(--muted)}
.topline span{margin-right:22px}
.topline .ico{display:inline-block;width:10px;height:10px;background:var(--blue);border-radius:50%;margin-right:6px;vertical-align:middle}
.auth a{color:var(--blue);text-decoration:none;margin-left:16px;font-weight:600}
.main-nav{height:53px;display:flex;justify-content:space-between;align-items:center}
.main-nav ul{list-style:none;display:flex}
.main-nav li{font-size:13px;font-weight:700;text-transform:uppercase;color:var(--navy);padding:0 18px;border-right:1px solid var(--line)}
.main-nav li:last-child{border-right:none}
.main-nav li.active{color:var(--blue)}
.brand{position:absolute;left:50%;top:4px;transform:translateX(-50%);width:150px;height:110px;background:var(--white);border-radius:0 0 12px 12px;display:flex;flex-direction:column;align-items:center;justify-content:center;z-index:3;box-shadow:0 3px 8px rgba(0,0,0,.12)}
.brand .mark{width:44px;height:44px;border-radius:50%;background:var(--blue)}
.brand .name{font-size:12px;font-weight:800;color:var(--blue-dark);text-transform:uppercase;margin-top:6px;letter-spacing:.5px}

/* hero */
.hero{height:464px;position:relative;background:linear-gradient(135deg,#c9d5e2 0%,#8fa4bd 45%,#52637c 100%)}
.hero-caption{position:absolute;left:0;right:0;bottom:0;height:82px;background:rgba(12,22,40,.78);display:flex;align-items:center}
.hero-caption h1{color:var(--white);font-size:25px;font-weight:800;text-transform:uppercase;line-height:1.3;width:900px}
.arrows{position:absolute;right:0;top:50%;transform:translateY(-50%);display:flex;gap:4px}
.arrows span{width:28px;height:28px;background:var(--blue);display:flex;align-items:center;justify-content:center}

/* welcome */
.welcome{padding:36px 0 30px;height:312px}
.welcome .wrap{display:flex;justify-content:space-between}
.welcome-text{width:650px}
.sec-title{font-size:22px;font-weight:800;text-transform:uppercase;color:var(--blue-dark);margin-bottom:12px}
.welcome-text p{color:var(--muted);font-size:13px;margin-bottom:16px}
.btn{display:inline-block;background:var(--blue);color:var(--white);font-size:11px;font-weight:700;text-transform:uppercase;padding:8px 16px;border-radius:2px}
.news{width:380px;border:1px solid var(--line);background:var(--pale)}
.news h3{background:var(--blue);color:var(--white);font-size:19px;font-weight:700;text-transform:uppercase;padding:10px 16px}
.news-item{padding:9px 16px;border-bottom:1px solid var(--line);font-size:11px}
.news-item b{display:block;color:var(--blue);font-weight:600}
.news-item span{color:var(--muted)}

/* courses */
.courses{background:var(--blue-dark);height:340px;padding-top:30px;margin-top:6px}
.courses .wrap{display:flex;justify-content:space-between}
.courses-intro{width:330px;color:#d5e3f5}
.courses-intro .sec-title{color:var(--white)}
.courses-intro p{font-size:12px;margin-bottom:18px}
.btn-ghost{display:inline-block;border:1px solid var(--white);color:var(--white);font-size:11px;font-weight:700;text-transform:uppercase;padding:7px 14px}
.course-card{width:350px;background:var(--white)}
.course-card .photo{height:150px}
.course-card .photo.biz{background:linear-gradient(135deg,#b9c4d2,#6d7f97)}
.course-card .photo.comp{background:linear-gradient(135deg,#c6d7e8,#5f86ad)}
.course-card .body{padding:12px 14px}
.course-card h4{font-size:15px;font-weight:700;color:var(--blue);text-transform:uppercase;margin-bottom:4px}
.course-card p{font-size:11px;color:var(--muted);margin-bottom:8px}
.course-card .more{font-size:11px;font-weight:700;color:var(--blue-dark);text-transform:uppercase}

/* mission */
.mission{padding:50px 0 40px}
.mission-box{border:2px solid var(--blue);padding:18px 50px;text-align:center}
.mission-box .sec-title{margin-bottom:8px}
.mission-box p{font-size:12px;color:var(--muted)}

/* values */
.values{height:388px;background:linear-gradient(180deg,var(--sky),var(--blue));padding-top:34px;color:var(--white)}
.values .sec-title{color:var(--white);text-align:center;margin-bottom:30px}
.values-grid{display:grid;grid-template-columns:repeat(3,1fr);gap:38px 40px}
.value{display:flex;gap:14px}
.value .badge{flex:none;width:42px;height:42px;border-radius:50%;background:var(--white);display:flex;align-items:center;justify-content:center}
.value h5{font-size:15px;font-weight:700}
.value p{font-size:11px;color:#e3f0fb}

/* testimonials */
.testimonials{padding:40px 0 0;height:456px}
.testimonials .sec-title{text-align:center;margin-bottom:30px}
.quotes{display:flex;justify-content:space-between}
.quote{width:340px;text-align:center}
.quote .box{border:1px solid var(--line);background:var(--pale);padding:22px 20px;font-size:12px;color:var(--muted);font-style:normal;position:relative}
.quote .box:after{content:"";position:absolute;left:50%;bottom:-9px;width:16px;height:16px;background:var(--pale);border-right:1px solid var(--line);border-bottom:1px solid var(--line);transform:translateX(-50%) rotate(45deg)}
.quote .who{margin-top:22px;font-size:13px;font-weight:700;color:var(--blue)}
.quote .role{font-size:11px;color:var(--muted)}

/* footer */
.site-footer{background:var(--navy);height:174px;color:#aeb9c9;position:absolute;left:0;right:0;top:2278px}
.foot-cols{display:flex;justify-content:space-between;padding-top:20px;height:140px}
.foot-col{width:170px}
.foot-col h6{font-size:12px;font-weight:700;color:var(--white);text-transform:uppercase;margin-bottom:6px}
.foot-col ul{list-style:none;font-size:11px;line-height:1.75}
.newsletter{width:240px}
.newsletter .field{display:flex;margin-bottom:12px}
.newsletter .input{flex:1;background:var(--white);height:26px;font-size:11px;color:var(--muted);padding:5px 8px}
.newsletter .go{background:var(--blue);color:var(--white);font-size:11px;font-weight:700;padding:5px 10px}
.follow{font-size:12px;color:var(--white);font-weight:700;margin-bottom:6px}
.socials{display:flex;gap:8px}
.socials span{width:22px;height:22px;border-radius:50%;background:var(--blue)}
.copy{background:var(--navy-deep);height:34px;text-align:center;font-size:11px;line-height:34px}
</style>
</head>
<body>

<header class="site-header">
  <div class="wrap">
    <div class="topline">
      <div><span><i class="ico"></i>+250 200 555 014</span><span><i class="ico"></i>info@lanterninstitute.org</span></div>
      <div class="auth"><a>Sign Up</a><a>Log In</a></div>
    </div>
    <nav class="main-nav">
      <ul><li class="active">Home</li><li>Our Courses Offered</li></ul>
      <ul><li>Core Values</li><li>Latest News</li><li>Contact Us</li></ul>
    </nav>
  </div>
  <div class="brand"><div class="mark"></div><div class="name">Lantern</div></div>
</header>

<section class="hero" role="img" aria-label="Photo of smiling students and a lecturer gathered around a laptop">
  <div class="hero-caption">
    <div class="wrap">
      <h1>We are an institute which focus on business courses and computer course...</h1>
      <div class="arrows">
        <span><svg width="10" height="12" viewBox="0 0 10 12"><path d="M8 1 2 6l6 5" fill="none" stroke="#fff" stroke-width="2"/></svg></span>
        <span><svg width="10" height="12" viewBox="0 0 10 12"><path d="M2 1l6 5-6 5" fill="none" stroke="#fff" stroke-width="2"/></svg></span>
      </div>
    </div>
  </div>
</section>

<section class="welcome">
  <div class="wrap">
    <div class="welcome-text">
      <h2 class="sec-title">Welcome to our website</h2>
      <p>Lantern Institute of Business and Technology (LIBT) is a fast growing education and training provider focusing on practical knowledge and skills that employers value. It is committed to the core values of creating meaningful and measurable differences in careers and growth through innovative learning and knowledge management. We prepare students not only for professional careers but also to embrace the importance of discipline, respect, integrity and lifelong learning in every field they choose to pursue.</p>
      <span class="btn">Read More</span>
    </div>
    <aside class="news">
      <h3>News Updates</h3>
      <div class="news-item"><b>New evening classes open for enrolment</b><span>Short courses in accounting and office skills start next month.</span></div>
      <div class="news-item"><b>Free online study resources now live</b><span>Students can reach open notes and practice tests any time.</span></div>
      <div class="news-item"><b>Career day set for the coming term</b><span>Meet local employers and learn about job placement routes.</span></div>
    </aside>
  </div>
</section>

<section class="courses">
  <div class="wrap">
    <div class="courses-intro">
      <h2 class="sec-title">Our Courses Offered</h2>
      <p>Our programmes cover business and computer studies as well as vocational training for employment. Each course is designed with industry input so learners gain hands on skills, confidence and the qualifications they need for career development and advancement in a changing market.</p>
      <span class="btn-ghost">View All Courses</span>
    </div>
    <article class="course-card">
      <div class="photo biz" role="img" aria-label="Photo of business students in a classroom"></div>
      <div class="body">
        <h4>Business Courses</h4>
        <p>Accounting, management, marketing and entrepreneurship taught by experienced practitioners.</p>
        <span class="more">Learn More</span>
      </div>
    </article>
    <article class="course-card">
      <div class="photo comp" role="img" aria-label="Photo of students working at computers"></div>
      <div class="body">
        <h4>Computer Courses</h4>
        <p>Office applications, networking, programming and design skills for the digital workplace.</p>
        <span class="more">Learn More</span>
      </div>
    </article>
  </div>
</section>

<section class="mission">
  <div class="wrap">
    <div class="mission-box">
      <h2 class="sec-title">Our Mission</h2>
      <p>To bridge the gap between academia and industry requirements and develop a directly employable workforce. Empower our students to go through intellectual, social and personal transformation, and to transform their competence to employable strength that meets the reporting of applied skills.</p>
    </div>
  </div>
</section>

<section class="values">
  <div class="wrap">
    <h2 class="sec-title">Our Core Values</h2>
    <div class="values-grid">
      <div class="value"><span class="badge"><svg width="18" height="18" viewBox="0 0 18 18"><path d="M3 9l4 4 8-9" fill="none" stroke="#1f6fc5" stroke-width="2.4"/></svg></span><div><h5>Excellence</h5><p>Excellence in teaching, research, creative endeavour and service in all aspects of the institution.</p></div></div>
      <div class="value"><span class="badge"><svg width="18" height="18" viewBox="0 0 18 18"><path d="M3 9l4 4 8-9" fill="none" stroke="#1f6fc5" stroke-width="2.4"/></svg></span><div><h5>Integrity</h5><p>Honesty and fairness in teaching, research, creative endeavour and service in all aspects of the institution.</p></div></div>
      <div class="value"><span class="badge"><svg width="18" height="18" viewBox="0 0 18 18"><path d="M3 9l4 4 8-9" fill="none" stroke="#1f6fc5" stroke-width="2.4"/></svg></span><div><h5>Respect</h5><p>Respect for every learner, colleague and partner in teaching, service and all aspects of the institution.</p></div></div>
      <div class="value"><span class="badge"><svg width="18" height="18" viewBox="0 0 18 18"><path d="M3 9l4 4 8-9" fill="none" stroke="#1f6fc5" stroke-width="2.4"/></svg></span><div><h5>Discipline Innovation</h5><p>Disciplined and creative thinking in teaching, research and service in all aspects of the institution.</p></div></div>
      <div class="value"><span class="badge"><svg width="18" height="18" viewBox="0 0 18 18"><path d="M3 9l4 4 8-9" fill="none" stroke="#1f6fc5" stroke-width="2.4"/></svg></span><div><h5>Bias for Action</h5><p>Taking action quickly in teaching, research, creative endeavour and service in all aspects of the institution.</p></div></div>
      <div class="value"><span class="badge"><svg width="18" height="18" viewBox="0 0 18 18"><path d="M3 9l4 4 8-9" fill="none" stroke="#1f6fc5" stroke-width="2.4"/></svg></span><div><h5>Customer Obsession</h5><p>Putting students first in teaching, research, creative endeavour and service in all aspects of the institution.</p></div></div>
    </div>
  </div>
</section>

<section class="testimonials">
  <div class="wrap">
    <h2 class="sec-title">Our Testimonials</h2>
    <div class="quotes">
      <div class="quote"><div class="box">“ The business diploma gave me practical skills I use every day at work. The lecturers were patient and helpful, and the career team supported me until I found a good job. I recommend the institute to anyone. ”</div><div class="who">Dana Okoro</div><div class="role">Digital Marketing</div></div>
      <div class="quote"><div class="box">“ The business diploma gave me practical skills I use every day at work. The lecturers were patient and helpful, and the career team supported me until I found a good job. I recommend the institute to anyone. ”</div><div class="who">Dana Okoro</div><div class="role">Digital Marketing</div></div>
      <div class="quote"><div class="box">“ The business diploma gave me practical skills I use every day at work. The lecturers were patient and helpful, and the career team supported me until I found a good job. I recommend the institute to anyone. ”</div><div class="who">Dana Okoro</div><div class="role">Digital Marketing</div></div>
    </div>
  </div>
</section>

<footer class="site-footer">
  <div class="wrap foot-cols">
    <div class="foot-col"><h6>Quick Links</h6><ul><li>Home</li><li>About Us</li><li>Our Courses Offered</li><li>Core Values</li><li>Latest News</li></ul></div>
    <div class="foot-col"><h6>Courses Offered</h6><ul><li>Business courses</li><li>Computer courses</li><li>Vocational training</li><li>Career development</li><li>Online resources</li></ul></div>
    <div class="foot-col"><h6>&nbsp;</h6><ul><li>Free study materials</li><li>Practice tests</li><li>Open library</li><li>Student guides</li><li>Study forum</li></ul></div>
    <div class="foot-col"><h6>Privacy Policy</h6><ul><li>Terms of use</li><li>Privacy policy</li><li>Refund policy</li><li>FAQ</li><li>Contact us</li></ul></div>
    <div class="newsletter">
      <h6 class="foot-col" style="width:auto;font-size:12px;font-weight:700;color:#fff;text-transform:uppercase;margin-bottom:6px">Newsletter Signup</h6>
      <div class="field"><span class="input">Enter email address</span><span class="go">Sign Up</span></div>
      <div class="follow">Follow Us</div>
      <div class="socials"><span></span><span></span><span></span><span></span></div>
    </div>
  </div>
  <div class="copy">© 2024 Lantern Institute of Business and Technology. All rights reserved.</div>
</footer>

</body>
</html>
```